Navigate the Underground Car Park to 7K3R Vet Clinic

Eye-catching signage for Underground Carpark.
We want to help new Clients, or those with bad senses of direction, to the correct Lift Lobby.
We want to be able to say 'Just follow the signs'.

It can be confusing and many other business have utilised some of the pillars in the carpark to guide their customers to the right place.

People don't want to walk far with sick animals so it is important they get to the right Lift Lobby.
Updates

We are thinking instead of 'Just Follow the Signs,We would like to try:'Looking for us?' (Large Text)'Follow the Signs (much smaller Text)Also, it is very useful to see the proposed sign dropped on to the photo of the car park pillars I included.Many thanks Added Friday, June 16, 2017

Target Market(s)

Customers, coming for the 1st time, trying to navigate the Underground CarPark towards the appropriate Lift lobby

Industry/Entity Type

Veterinary

Font styles to use
Serif

Colors
f78f20
00a990
0455a3

Requirements
Must have
• Logo.
• Bright. Clear. Not too cluttered.
• Warmth. Humour. Approachable.
• Please include: Building 4, Mezzanine Level
Nice to have
• Please look at our FB pages and Instagram page @7k3rvetclinic for a good feel of who we are.
• Some level of style or image continuity with the Pet Tips Poster (see attached file)
Should not have
• Not have a medical feel

```html
<!DOCTYPE html>
<html lang="en">
<head>
<meta charset="utf-8">
<title>7K3R Vet Clinic – Car Park Wayfinding Sign</title>
<link rel="stylesheet" href="https://fonts.googleapis.com/css2?family=Old+Standard+TT:wght@400;700&display=swap">
<style>
  :root {
    --orange: #f78f20;
    --teal: #00a990;
    --blue: #0455a3;
    --ink: #2a1f5c;
    --white: #ffffff;
    --paper: #fbf8f3;
    --frame: #0b0b0b;
    --backdrop: #e9e9e7;
  }
  html, body {
    margin: 0;
    padding: 0;
    width: 1200px;
    height: 1200px;
    overflow: hidden;
    background: var(--backdrop);
  }
  .sign {
    position: absolute;
    left: 262px;
    top: 67px;
    width: 648px;
    height: 1037px;
    border: 14px solid var(--frame);
    background: var(--paper);
  }
  .sign__art {
    display: block;
    width: 648px;
    height: 1037px;
  }
  .brand-name,
  .headline,
  .subline,
  .location {
    font-family: "Old Standard TT", Georgia, serif;
  }
  .brand-name { fill: var(--white); font-weight: 700; font-size: 44px; }
  .headline { fill: var(--white); font-weight: 400; font-size: 88px; }
  .subline { fill: var(--ink); font-weight: 700; font-size: 44px; }
  .location { fill: var(--white); font-weight: 700; font-size: 26px; }
</style>
</head>
<body>
  <div class="sign">
    <svg class="sign__art" viewBox="0 0 648 1037" xmlns="http://www.w3.org/2000/svg">
      <defs>
        <linearGradient id="pet-photo-tone" x1="0" y1="0" x2="0" y2="1">
          <stop offset="0" stop-color="#e2c297"/>
          <stop offset="1" stop-color="#efe2cc"/>
        </linearGradient>
      </defs>

      <rect class="pattern-field" x="0" y="150" width="648" height="600" fill="#f3eee6"
            role="img" aria-label="Soft repeating pattern of pastel dog and cat silhouettes"/>

      <rect class="pet-photo" x="150" y="220" width="370" height="490"
            fill="url(#pet-photo-tone)" role="img" aria-label="Photo of a smiling tan dog with perked ears"/>

      <path class="header-band" d="M0 0 H648 V180 L120 318 Q30 338 0 262 Z" fill="var(--orange)"/>

      <rect class="brand-mark" x="196" y="88" width="30" height="30" fill="var(--white)"/>
      <text class="brand-name" x="590" y="118" text-anchor="end">7K3R Vet Clinic</text>

      <path class="footer-accent" d="M420 630 L565 580 Q630 560 648 620 V700 Q630 610 580 605 Z" fill="var(--teal)"/>
      <path class="footer-band" d="M0 715 L560 598 Q625 585 640 640 L648 680 V1037 H0 Z" fill="var(--blue)"/>

      <path class="direction-arrow" d="M97 657 L13 791 H58 V930 Q58 996 124 996 H612 V927 H170 Q129 927 129 890 V791 H174 Z"
            fill="var(--orange)" stroke="var(--white)" stroke-width="2" stroke-dasharray="1 3" stroke-linecap="round"/>

      <text class="headline" x="603" y="748" text-anchor="end">LOOKING</text>
      <text class="headline" x="603" y="840" text-anchor="end">FOR US?</text>
      <text class="subline" x="603" y="896" text-anchor="end">Follow the Signs</text>
      <text class="location" x="598" y="972" text-anchor="end">BUILDING 4, MEZZANINE LEVEL</text>
    </svg>
  </div>
</body>
</html>
```